BRANDHILL real estate family office

Hello, Our business is a real estate intermediation activity on high-end goods (amounts exceeding € 10m) for corporate and private clients. You can see our logo on the site www.brandhill-demo.fr We would like to keep that spirit with the hexagon that represents France (transactions between Monaco and Saint Tropez, Courchevel and Paris). And the "baseline" that is "real estate family office". The corporate logo should be and can be printed by embossing (relief). We must integrate the name, first name, phone, email and website. Finally, to imbibe the spirit of business, here is a detail of the activity. "Genuine consulting firm in real estate investments, BRANDHILL works with its customers as a specialized player in the high-end markets, we are recognized for our ultra-confidential approach and tailor-made, as well as the quality of our network. We broadcast any information on the market and we work exclusively through a strong relationship we have developed over the years. BRANDHILL is active on the French Riviera (from Monaco to Saint-Tropez), the Alps (Courchevel, Méribel, Megève) and Paris (essentially market premium). Always looking for opportunities for our clients, we work on two investment areas: residential luxury real estate (properties, vineyards, mansions, land, etc.) commercial real estate (empty office buildings or yield, hotel properties, land, etc.) "

Target Market(s)

High foreign end customers. corporate and private.

Industry/Entity Type

Real Estate

Contact Information for Business Card

LOGO
baseline
Laurent Dufossé
+33(0)6.41.57.09.64
ld@brandhill-demo.fr
www.brandhill-demo.fr

Font styles to use
Serif

Colors
cedeed
0255a3
3277b5
85abd2
85cae6
34a7d7
0792cd
cfdeed
1b1b1b

Requirements
Must have
• see description

```html
<!DOCTYPE html>
<html lang="fr">
<head>
<meta charset="utf-8">
<title>BRANDHILL – cartes de visite</title>
<link href="https://fonts.googleapis.com/css2?family=Quicksand:wght@400;500&display=swap" rel="stylesheet">
<style>
  :root {
    --backdrop: #e4ddd2;
    --card-white: #ffffff;
    --brand-blue: #1f35a0;
    --ink: #1b1b1b;
    --logo-grey: #4a4d55;
    --emboss: #dcdcdc;
  }
  * { margin: 0; padding: 0; box-sizing: border-box; }
  html, body {
    width: 1200px; height: 1200px; overflow: hidden;
    background: var(--backdrop);
    font-family: "Quicksand", sans-serif;
  }
  .canvas { position: relative; width: 1200px; height: 1200px; }
  .card {
    position: absolute; left: 287px; width: 626px; height: 390px;
  }
  .card--front { top: 150px; background: var(--card-white); }
  .card--back {
    top: 681px; background: var(--brand-blue);
    display: flex; align-items: center; justify-content: center;
  }
  .brand {
    position: absolute; right: 16px; top: 24px; text-align: right;
  }
  .brand__name {
    display: block;
    font-size: 38px; font-weight: 400; letter-spacing: 4px;
    color: var(--logo-grey); line-height: 1;
  }
  .brand__baseline {
    display: block; margin-top: 6px; margin-right: 4px;
    font-size: 12px; font-weight: 500; letter-spacing: 1px;
    color: var(--brand-blue);
  }
  .identity {
    position: absolute; left: 24px; top: 220px; height: 62px;
    padding-left: 20px; border-left: 10px solid var(--brand-blue);
  }
  .identity__name {
    font-size: 31px; font-weight: 400; color: var(--ink);
    line-height: 1; margin-top: 6px;
  }
  .identity__title {
    font-size: 18px; font-weight: 400; color: var(--ink); margin-top: 2px;
  }
  .contact {
    position: absolute; left: 22px; top: 318px; list-style: none;
  }
  .contact__item {
    display: flex; align-items: center; gap: 5px;
    font-size: 18px; color: var(--ink); height: 32px;
  }
  .contact__icon { width: 17px; height: 14px; fill: var(--brand-blue); }
  .back-brand {
    font-size: 44px; font-weight: 500; letter-spacing: 6px;
    color: var(--emboss);
  }
</style>
</head>
<body>
<main class="canvas">
  <section class="card card--front">
    <div class="brand">
      <span class="brand__name">BRANDHILL</span>
      <span class="brand__baseline">real estate family office</span>
    </div>
    <div class="identity">
      <p class="identity__name">Laurent Dufossé</p>
      <p class="identity__title">Job Title</p>
    </div>
    <ul class="contact">
      <li class="contact__item">
        <svg class="contact__icon" viewBox="0 0 17 14" aria-hidden="true">
          <path d="M1 4 Q8.5 -1 16 4 L16 6 L12 6 L12 4 Q8.5 3 5 4 L5 6 L1 6 Z"/>
          <path d="M4 7 L13 7 L15 13 L2 13 Z"/>
        </svg>
        +33(0)6 41 57 09 64
      </li>
      <li class="contact__item">
        <svg class="contact__icon" viewBox="0 0 17 14" aria-hidden="true">
          <path d="M1 3 L16 3 L16 12 L1 12 Z M2 4 L8.5 8.5 L15 4 Z" fill-rule="evenodd"/>
        </svg>
        ld@brandhill-demo.fr
      </li>
    </ul>
  </section>

  <section class="card card--back">
    <span class="back-brand">BRANDHILL</span>
  </section>
</main>
</body>
</html>
```